Q R Ventral Harbor Works, LLC
I just posted pic to use....
where we can find the details for this project....can u upload it in pdf format...so we can start designing it..
Sorry looking for a Trifold brochure

```html
<!DOCTYPE html>
<html lang="en">
<head>
<meta charset="utf-8">
<title>Q R Ventral Harbor Works — Stationery Suite</title>
<link href="https://fonts.googleapis.com/css2?family=Open+Sans:wght@400;600;700&family=Tinos&display=swap" rel="stylesheet">
<style>
:root{
  --bg:#ece7df;
  --amber:#d98a0e;
  --amber-light:#f3b53a;
  --amber-deep:#8c4806;
  --cream:#fff6e2;
  --ink:#3a2a12;
  --white:#ffffff;
  --photo-a:#8b8f96;
  --photo-b:#c9ccd1;
}
*{box-sizing:border-box;margin:0;padding:0}
html,body{width:1200px;height:685px;overflow:hidden}
body{background:var(--bg);font-family:"Open Sans",Arial,sans-serif;color:var(--cream);position:relative}
.piece{position:absolute;overflow:hidden;box-shadow:0 2px 6px rgba(0,0,0,.25)}
.amber{background:linear-gradient(135deg,var(--amber-light) 0%,var(--amber) 45%,var(--amber-deep) 100%)}
.amber-flat{background:linear-gradient(180deg,var(--amber) 0%,var(--amber-deep) 100%)}
.caption{position:absolute;font-family:"Tinos",serif;font-size:11px;letter-spacing:.5px;color:#5b4a33;text-transform:uppercase}
.brand{display:flex;align-items:center;gap:6px;font-weight:700;color:var(--amber-deep)}
.brand .dot{border-radius:50%;background:var(--amber);flex:none}
.brand.light{color:var(--cream)}
.brand.light .dot{background:var(--cream)}
.photo{background:linear-gradient(160deg,var(--photo-b),var(--photo-a))}
.copy{font-size:5px;line-height:1.45}
.copy p{margin-bottom:4px}
h3{font-size:7px;font-weight:700;color:var(--white);margin-bottom:3px;text-transform:uppercase}
h4{font-size:6px;font-weight:700;color:var(--cream);margin-bottom:2px}
.abs{position:absolute}

/* folder back */
.folder-back{left:80px;top:29px;width:400px;height:247px;display:flex}
.folder-back .side{width:108px}
.folder-back .panel{width:209px;background:var(--white);position:relative}
.folder-back .side.right{width:83px}
.folder-back .brand{position:absolute;left:40px;top:90px;font-size:11px}
.folder-back .brand .dot{width:44px;height:44px}
.folder-back .address{position:absolute;left:10px;bottom:20px;width:90px}

/* folder inside */
.folder-inside{left:504px;top:29px;width:389px;height:247px}
.folder-inside .sheet{left:156px;top:0;width:144px;height:200px;background:var(--white)}
.folder-inside .pocket{left:156px;top:160px;width:233px;height:87px;border-top:2px solid var(--amber-light)}
.folder-inside .pocket .brand{position:absolute;left:48px;top:14px}
.folder-inside .pocket .dot{width:40px;height:40px}
.folder-inside .flap{left:300px;top:0;width:89px;height:160px;background:linear-gradient(90deg,var(--amber-deep),var(--amber))}

/* flyer */
.flyer{left:907px;top:24px;width:221px;height:300px;padding:10px}
.flyer .brand{justify-content:flex-end;font-size:8px}
.flyer .brand .dot{width:22px;height:22px}
.flyer .copy{margin-top:10px}
.flyer .strip{display:flex;gap:3px;margin:8px 0}
.flyer .strip div{flex:1;height:34px}

/* brochure front */
.brochure-front{left:36px;top:343px;width:389px;height:293px;display:flex}
.brochure-front .fold{width:130px;height:100%;position:relative;padding:10px 8px}
.brochure-front .fold + .fold{border-left:1px solid rgba(0,0,0,.15)}
.brochure-front .firm{font-size:6px;font-weight:700;color:var(--white);margin-bottom:8px}
.brochure-front .keys{left:0;bottom:0;width:100%;height:70px;background:linear-gradient(180deg,transparent,rgba(90,45,5,.55))}
.brochure-front .contact .dot{width:50px;height:50px;border-radius:50%;background:var(--cream);margin:4px auto 12px}
.brochure-front .contact h3 .mark{display:inline-block;width:6px;height:6px;border-radius:50%;background:var(--white);margin-right:3px}
.brochure-front .cover{padding:0;background:var(--white)}
.brochure-front .cover .brand{padding:28px 10px 8px;font-size:10px}
.brochure-front .cover .brand .dot{width:14px;height:14px}
.brochure-front .cover .photo{height:90px;margin:0 0 0 8px}
.brochure-front .cover .base{left:0;bottom:0;width:100%;height:150px}

/* brochure inside */
.brochure-inside{left:432px;top:343px;width:449px;height:293px;display:flex}
.brochure-inside .fold{width:150px;height:100%;padding:10px 8px;border-left:1px solid rgba(0,0,0,.15)}
.brochure-inside .fold:first-child{border-left:none}
.brochure-inside .photo.small{width:40px;height:30px;float:left;margin:0 5px 3px 0}
.brochure-inside .photo.wide{height:50px;margin-top:6px}
.brochure-inside .row{overflow:hidden;margin-bottom:6px}
</style>
</head>
<body>

<!-- Folder back -->
<section class="piece folder-back">
  <div class="side amber"></div>
  <div class="panel">
    <div class="brand"><span class="dot"></span>QR Ventral</div>
    <svg class="abs" style="left:0;bottom:0" width="209" height="40" viewBox="0 0 209 40"><path d="M0 30 Q100 10 209 24 L209 40 L0 40Z" fill="#d98a0e"/><path d="M0 26 Q100 6 209 20" stroke="#f3b53a" stroke-width="2" fill="none"/></svg>
  </div>
  <div class="side right amber"></div>
</section>
<div class="abs copy" style="left:90px;top:230px;width:92px">Q R Ventral Harbor Works, LLC<br>12 Marlow Court, Suite 4<br>Avenfield, TX 75001</div>
<span class="caption" style="left:245px;top:292px">Folder Back</span>

<!-- Folder inside -->
<section class="piece folder-inside amber">
  <div class="abs sheet"></div>
  <div class="abs flap"></div>
  <div class="abs pocket amber">
    <div class="brand light"><span class="dot"></span></div>
  </div>
</section>
<span class="caption" style="left:660px;top:292px">Folder Inside</span>

<!-- Flyer -->
<section class="piece flyer amber">
  <div class="brand light"><span class="dot"></span>QR Ventral</div>
  <div class="copy">
    <p>Q R Ventral Harbor Works, LLC helps growing firms plan, build and run steady operations. We bring clear strategy and hands-on support to every partner.</p>
    <p>Our team works side by side with leaders to shape goals, test ideas and turn plans into lasting results across each department.</p>
  </div>
  <div class="strip">
    <div class="photo" role="img" aria-label="Team meeting photo"></div>
    <div class="photo" role="img" aria-label="Business people at table photo"></div>
    <div class="photo" role="img" aria-label="Consultants talking photo"></div>
  </div>
  <div class="copy"><p>Call 555-0142 or write to hello@qrventral.com to book a first session.</p></div>
</section>
<span class="caption" style="left:1000px;top:333px">Flyer</span>

<!-- Brochure front -->
<section class="piece brochure-front">
  <div class="fold amber">
    <div class="firm">Q R Ventral Harbor Works, LLC</div>
    <div class="copy">
      <p>We guide companies through change with plain advice and careful planning.</p>
      <p>From first review to final delivery, our people stay close to yours.</p>
      <p>Every plan is built around your market and your goals.</p>
    </div>
    <div class="abs keys" role="img" aria-label="Faint keyboard photo"></div>
  </div>
  <div class="fold amber-flat contact">
    <div class="dot"></div>
    <h3><span class="mark"></span>Contact Us</h3>
    <div class="copy">
      <p>12 Marlow Court, Suite 4<br>Avenfield, TX 75001</p>
      <p>Phone: 555-0142<br>Fax: 555-0143</p>
      <p>hello@qrventral.com<br>www.qrventral.com</p>
    </div>
  </div>
  <div class="fold cover">
    <div class="brand"><span class="dot"></span>QR Ventral</div>
    <div class="abs base amber"></div>
    <div class="photo abs" style="left:8px;top:70px;width:122px;height:90px" role="img" aria-label="Business team in meeting photo"></div>
  </div>
</section>
<span class="caption" style="left:175px;top:648px">Brochure Front</span>

<!-- Brochure inside -->
<section class="piece brochure-inside amber">
  <div class="fold">
    <h3>Services</h3>
    <div class="row"><div class="photo small" role="img" aria-label="Office work photo"></div><div class="copy">Planning, review and growth support for firms of every size.</div></div>
    <div class="copy">
      <p>We study how your company runs today and map the steps toward where it needs to be.</p>
      <p>Each service is shaped to your team and budget.</p>
    </div>
  </div>
  <div class="fold">
    <h4>Why Work With Us</h4>
    <div class="copy"><p>Clear thinking, honest advice and steady follow-through on every project we take.</p></div>
    <h4>Reliable, Proven, Executed</h4>
    <div class="copy"><p>Our record shows plans that are carried out on time and measured with care.</p></div>
    <h4>Our Approach</h4>
    <div class="copy"><p>Listen first, then build together.</p></div>
    <div class="photo wide" role="img" aria-label="Two business people portrait photo"></div>
  </div>
  <div class="fold">
    <h4>Mission and Objectives</h4>
    <div class="row"><div class="photo small" role="img" aria-label="Meeting room photo"></div><div class="copy">Help leaders make sound choices and grow with confidence.</div></div>
    <div class="row"><div class="photo small" role="img" aria-label="Handshake photo"></div><div class="copy">Build lasting ties with every client we serve.</div></div>
    <div class="row"><div class="photo small" role="img" aria-label="Team at work photo"></div><div class="copy">Deliver results that can be seen and counted.</div></div>
  </div>
</section>
<span class="caption" style="left:605px;top:648px">Brochure Inside</span>

</body>
</html>
```